Travinex - You are the Boss!

Travinex is a new Silicon Valley company, of the pelim founders from Berlin, which provides a "Shared Pioneer Circle". This platform allows the crowd to support startups with money, experts and fame. Our Vision is, that everyone should become an entrepreneur.

Pls find all brief details in the attached document
Updates

Would be nice to have a list of more social services I'm available on, like a list of pictograms of all my services:

Find me on: vooka, bramlet+, qrt, fenwix, moodrail, zupp, hvoxa, etc...

pls make sure to use the right font:
http://www.typemarlow.com/fonts/Velquin

Target Market(s)

Main target market is those already involved in the startup industry, by fundraising, investing, advising, cofounding and working. Travinex brings a totaly new transparency and collaborative way of starting companies to that business.

· Entrepreneurs (looking for funding, team and community)
· Investors (looking for hot investments and )
· Experts (workers looking for startups they can work for equity)
· Incubators & Business Schools (looking for tools to advise startups)

Industry/Entity Type

It Company

Requirements
Must have
• Pls find all brief details in the attached document
Nice to have

```html
<!DOCTYPE html>
<html lang="en">
<head>
<meta charset="utf-8">
<title>Travinex – Business Card</title>
<link rel="stylesheet" href="https://fonts.googleapis.com/css2?family=Orbitron:wght@400;500&display=swap">
<style>
  :root {
    --canvas-bg: #ffffff;
    --card-dark: #333333;
    --card-edge: #8e2a22;
    --frame-line: #111111;
    --brand-orange: #f26a3a;
    --brand-cyan: #4fb8c9;
    --text-light: #ffffff;
    --panel-cream: #fde9df;
    --guide-grey: #b9a49a;
  }
  html, body {
    margin: 0;
    padding: 0;
    width: 1200px;
    height: 944px;
    overflow: hidden;
    background: var(--canvas-bg);
    font-family: "Orbitron", sans-serif;
  }
  .canvas {
    position: relative;
    width: 1200px;
    height: 944px;
  }

  /* Front side */
  .card-front {
    position: absolute;
    left: 10px;
    top: 6px;
    width: 554px;
    height: 936px;
    box-sizing: border-box;
    background: var(--card-dark);
    border: 2px solid var(--card-edge);
  }
  .card-front .trim-frame {
    position: absolute;
    left: 29px;
    top: 29px;
    width: 501px;
    height: 875px;
    box-sizing: border-box;
    border: 1px solid var(--frame-line);
  }
  .contact-block {
    position: absolute;
    right: 52px;
    top: 52px;
    text-align: right;
    white-space: nowrap;
  }
  .person-name {
    margin: 0;
    color: var(--brand-orange);
    font-size: 35px;
    font-weight: 400;
    line-height: 1.2;
  }
  .person-role {
    margin: 28px 0 0;
    color: var(--brand-cyan);
    font-size: 19px;
    line-height: 1.25;
  }
  .person-detail {
    margin: 0;
    color: var(--text-light);
    font-size: 17px;
    line-height: 1.4;
  }
  .social-list {
    list-style: none;
    margin: 14px 0 0;
    padding: 0;
  }
  .social-item {
    display: flex;
    justify-content: flex-end;
    align-items: center;
    gap: 10px;
    height: 39px;
    color: var(--text-light);
    font-size: 17px;
  }
  .social-mark {
    width: 23px;
    height: 23px;
    border-radius: 3px;
    background: var(--brand-cyan);
  }
  .brand-block {
    position: absolute;
    left: 62px;
    top: 620px;
    white-space: nowrap;
  }
  .brand-name {
    display: flex;
    align-items: center;
    gap: 14px;
    margin: 0;
    color: var(--brand-cyan);
    font-size: 38px;
    font-weight: 400;
    letter-spacing: 1px;
    line-height: 1.1;
  }
  .brand-dot {
    width: 24px;
    height: 24px;
    border-radius: 50%;
    background: var(--brand-orange);
  }
  .brand-tagline {
    margin: 4px 0 0 27px;
    color: var(--text-light);
    font-size: 22px;
  }
  .website {
    position: absolute;
    left: 59px;
    top: 848px;
    margin: 0;
    color: var(--brand-orange);
    font-size: 31px;
    white-space: nowrap;
  }

  /* Back side */
  .card-back {
    position: absolute;
    left: 636px;
    top: 6px;
    width: 547px;
    height: 936px;
    background: var(--brand-orange);
  }
  .card-back svg {
    display: block;
  }
  .back-text {
    font-family: "Orbitron", sans-serif;
    font-size: 21px;
  }
  .text-orange { fill: var(--brand-orange); }
  .text-cyan { fill: var(--brand-cyan); }
</style>
</head>
<body>
<main class="canvas">

  <section class="card-front" aria-label="Business card front">
    <div class="trim-frame"></div>

    <div class="contact-block">
      <h1 class="person-name">Lukas Brenner</h1>
      <p class="person-role">Founder and CEO</p>
      <p class="person-detail">The@travinex.com</p>
      <p class="person-detail">tel. 0198765432</p>
      <ul class="social-list">
        <li class="social-item">Chirpline.com/lukasbrenner <span class="social-mark"></span></li>
        <li class="social-item">Facepage.com/lukasbrenner <span class="social-mark"></span></li>
        <li class="social-item">linkhub.com/in/lukasbrenner <span class="social-mark"></span></li>
      </ul>
    </div>

    <div class="brand-block">
      <h2 class="brand-name">TRAVINEX <span class="brand-dot"></span></h2>
      <p class="brand-tagline">You are the boss!</p>
    </div>

    <p class="website">www.travinex.com</p>
  </section>

  <section class="card-back" aria-label="Business card back">
    <svg width="547" height="936" viewBox="0 0 547 936">
      <rect class="trim-guide" x="28" y="28" width="492" height="882" fill="none" stroke="var(--guide-grey)" stroke-width="1"/>
      <rect class="info-panel" x="50" y="53" width="443" height="829" rx="37" fill="var(--panel-cream)"/>

      <text class="back-text text-orange" x="87" y="842" transform="rotate(-90 87 842)"
            textLength="750" lengthAdjust="spacingAndGlyphs">Are you interested in Startups, Investments, Work?</text>
      <text class="back-text text-orange" x="123" y="467" text-anchor="middle" transform="rotate(-90 123 467)"
            textLength="572" lengthAdjust="spacingAndGlyphs">Join us on Facepage.com/Travinex</text>

      <text class="back-text" x="458" y="842" transform="rotate(-90 458 842)"
            textLength="760" lengthAdjust="spacingAndGlyphs"><tspan class="text-orange">Berlin - </tspan><tspan class="text-cyan">Lindenhof Platz 7 | 10117 Berlin | Germany</tspan></text>
      <text class="back-text" x="485" y="842" transform="rotate(-90 485 842)"
            textLength="760" lengthAdjust="spacingAndGlyphs"><tspan class="text-orange">Silicon Valley - </tspan><tspan class="text-cyan">218 N Orchard Rd | Sunnyvale | CA 94086</tspan></text>
    </svg>
  </section>

</main>
</body>
</html>
```